Biz Cards to match new logo

I'm looking for a business card layout to go with my new logo. I'd like to have one side in colour (purple, with the logo in white) and the other side to be white with the purple logo and contact info in black font: name, address (2 lines), phone, email, fax, website. The logo includes the company name so it doesn't need to be repeated in the text. The font should be legibile to the semi-blind. (I hate small fonts on business cards).

Industry/Entity Type

Business

```html
<!DOCTYPE html>
<html lang="en">
<head>
<meta charset="utf-8">
<title>Business Card – Front</title>
<link rel="stylesheet" href="https://fonts.googleapis.com/css2?family=Open+Sans:wght@400;600;700&display=swap">
<style>
  :root {
    --brand-purple: #5223cc;
    --ink: #111111;
    --paper: #ffffff;
  }
  * { margin: 0; padding: 0; box-sizing: border-box; }
  html, body {
    width: 1200px;
    height: 702px;
    overflow: hidden;
    background: var(--paper);
  }
  .card {
    position: relative;
    width: 1200px;
    height: 702px;
    background: var(--paper);
    font-family: "Open Sans", Arial, sans-serif;
    color: var(--ink);
  }
  .brand-name {
    position: absolute;
    left: 52px;
    top: 78px;
    width: 190px;
    text-align: center;
    color: var(--brand-purple);
    font-weight: 600;
    font-size: 30px;
    line-height: 36px;
    letter-spacing: 3px;
  }
  .header-divider {
    position: absolute;
    left: 255px;
    top: 49px;
    width: 3px;
    height: 130px;
    background: var(--brand-purple);
  }
  .identity {
    position: absolute;
    left: 290px;
    top: 60px;
    width: 330px;
    text-align: center;
  }
  .identity .person-name {
    font-size: 41px;
    line-height: 54px;
    font-weight: 400;
  }
  .identity .designation {
    font-size: 36px;
    line-height: 48px;
    font-weight: 400;
    padding-left: 10px;
  }
  .accent-band {
    position: absolute;
    left: 0;
    top: 247px;
    width: 1200px;
    height: 16px;
    background: var(--brand-purple);
  }
  .contact-list {
    position: absolute;
    right: 61px;
    top: 298px;
    list-style: none;
    text-align: right;
    font-size: 31px;
  }
  .contact-list li { height: 60px; line-height: 44px; }
  .contact-list li:nth-child(3) { height: 52px; }
  .contact-list .label {
    color: var(--brand-purple);
    font-weight: 700;
  }
  .address-icon {
    position: absolute;
    left: 58px;
    top: 556px;
    width: 86px;
    height: 90px;
  }
  .address {
    position: absolute;
    left: 184px;
    top: 550px;
    font-size: 37px;
    line-height: 51px;
    font-style: normal;
  }
</style>
</head>
<body>
  <main class="card">
    <div class="brand-name">KELDRIM<br>LABS</div>
    <div class="header-divider"></div>
    <div class="identity">
      <p class="person-name">Name Goes Here</p>
      <p class="designation">Designation</p>
    </div>
    <div class="accent-band"></div>
    <ul class="contact-list">
      <li><span class="label">Mobile&nbsp; No</span> : 000-000-0000</li>
      <li><span class="label">Fax No</span> : 0000-000-0000</li>
      <li><span class="label">E-mail</span> : xyz@mailbox.com</li>
      <li><span class="label">Web</span> : www.xyz.com</li>
    </ul>
    <svg class="address-icon" viewBox="0 0 86 90" aria-hidden="true">
      <path d="M43 0 L86 38 L78 46 L43 15 L8 46 L0 38 Z" fill="var(--brand-purple)"/>
      <path d="M12 44 L43 18 L74 44 L74 90 L54 90 L54 66 Q54 56 43 56 Q32 56 32 66 L32 90 L12 90 Z" fill="var(--brand-purple)"/>
    </svg>
    <address class="address">
      Address Line 1<br>
      Address&nbsp; Line 2
    </address>
  </main>
</body>
</html>
```